Company service wheel graphic

A graphic demonstrating all the services the company offers.
I have hand drawn and written up on the attached the content that is required. Also attached is our company logo so you have a sense of the colour scheme of the logo.
This will eventually go into a company brochure, be used on our website etc.

Target Market(s)

Local GOvernment and other professionals who work in the sport, recreation and leisure industries

Industry/Entity Type

Sports, recreation, leisure, aquatics

Font styles to use
Other font styles liked:
• Calibri

Colors
0054AA
0677BA
7BADD7
CADEEF
E8F1F8

Requirements
Must have
• An eye catching graphic that captures all the information in the hand drawn atachement.
Nice to have
• Each quadrant in the circle to have its own colour, that links to the company logo

```html
<!DOCTYPE html>
<html lang="en">
<head>
<meta charset="utf-8">
<title>Service Wheel</title>
<link rel="stylesheet" href="https://fonts.googleapis.com/css2?family=Oswald:wght@500;600&display=swap">
<style>
  :root {
    --blue: #1077be;
    --navy: #262060;
    --white: #ffffff;
    --pale: #e8f1f8;
    --mist: #cadeef;
    --backdrop: #ececec;
  }
  html, body {
    margin: 0;
    width: 1200px;
    height: 1200px;
    overflow: hidden;
    background: var(--backdrop);
  }
  .stage {
    position: absolute;
    left: 0;
    top: 0;
    width: 1932px;
    height: 1932px;
    transform: scale(0.62112);
    transform-origin: 0 0;
    font-family: "Oswald", "Arial Narrow", sans-serif;
  }
  .wheel-art {
    position: absolute;
    left: 0;
    top: 0;
    width: 1932px;
    height: 1932px;
  }
  .service {
    position: absolute;
    margin: 0;
    padding-left: 24px;
    color: var(--white);
    font-weight: 500;
    font-size: 32px;
    line-height: 42px;
    white-space: nowrap;
  }
  .service::before {
    content: "";
    position: absolute;
    left: 0;
    top: 11px;
    border-left: 10px solid var(--white);
    border-top: 9px solid transparent;
    border-bottom: 9px solid transparent;
  }
  .service .cont { display: block; }
  .hub-title {
    position: absolute;
    margin: 0;
    color: var(--navy);
    font-weight: 600;
    text-align: center;
    white-space: nowrap;
  }
  .hub-title.top {
    left: 730px; width: 472px; top: 630px;
    font-size: 32px; line-height: 36px;
  }
  .hub-title.bottom {
    left: 730px; width: 472px; top: 1192px;
    font-size: 38px; line-height: 50px;
  }
  .hub-core {
    position: absolute;
    left: 830px; width: 284px; top: 876px;
    margin: 0;
    color: var(--navy);
    font-weight: 600;
    font-size: 38px;
    line-height: 34px;
    text-align: center;
  }
  .pillar {
    position: absolute;
    margin: 0;
    color: var(--white);
    font-weight: 500;
    font-size: 29px;
    line-height: 37px;
    white-space: nowrap;
  }
  .pillar.planning { left: 760px; top: 728px; }
  .pillar.management { right: 758px; top: 728px; text-align: right; }
  .pillar.participation { left: 748px; top: 1094px; }
  .pillar.impact { right: 746px; top: 1094px; text-align: right; }
</style>
</head>
<body>
<main class="stage">
  <svg class="wheel-art" viewBox="0 0 1932 1932" aria-hidden="true">
    <defs>
      <clipPath id="wheel-clip"><circle cx="966" cy="943" r="744"/></clipPath>
      <radialGradient id="core-fill" cx="0.45" cy="0.4" r="0.7">
        <stop offset="0" stop-color="#ffffff"/>
        <stop offset="0.7" stop-color="#f3f8fc"/>
        <stop offset="1" stop-color="#e1edf7"/>
      </radialGradient>
    </defs>
    <circle cx="966" cy="943" r="750" fill="var(--white)"/>
    <g clip-path="url(#wheel-clip)">
      <polygon class="quad planning-quad" fill="var(--blue)"
        points="0,0 966,0 966,370 917,415 966,465 966,943 487,943 438,995 390,943 0,943"/>
      <polygon class="quad management-quad" fill="var(--navy)"
        points="966,0 1932,0 1932,943 1542,943 1495,895 1448,943 966,943 966,465 917,415 966,370"/>
      <polygon class="quad impact-quad" fill="var(--blue)"
        points="966,943 1448,943 1495,895 1542,943 1932,943 1932,1932 966,1932 966,1520 1018,1470 966,1420"/>
      <polygon class="quad participation-quad" fill="var(--navy)"
        points="0,943 390,943 438,995 487,943 966,943 966,1420 1018,1470 966,1520 966,1932 0,1932"/>
      <g fill="none" stroke="var(--white)" stroke-width="6" stroke-linejoin="miter">
        <polyline points="966,190 966,370 917,415 966,465 966,943 966,1420 1018,1470 966,1520 966,1700"/>
        <polyline points="210,943 390,943 438,995 487,943 1448,943 1495,895 1542,943 1720,943"/>
      </g>
    </g>

    <rect x="730" y="624" width="472" height="638" fill="var(--white)"/>
    <rect x="736" y="714" width="226" height="226" fill="var(--navy)"/>
    <rect x="968" y="714" width="228" height="226" fill="var(--blue)"/>
    <rect x="736" y="946" width="226" height="228" fill="var(--blue)"/>
    <rect x="968" y="946" width="228" height="228" fill="var(--navy)"/>

    <g class="icon checklist" fill="none" stroke="var(--white)" stroke-width="4" stroke-linecap="round" stroke-linejoin="round">
      <rect x="768" y="778" width="56" height="62" rx="4"/>
      <path d="M778 792 l5 5 9 -9 M798 793 h18 M778 808 l5 5 9 -9 M798 809 h18 M778 824 l5 5 9 -9 M798 825 h8"/>
      <circle cx="818" cy="828" r="10"/>
      <path d="M818 822 v6 h5"/>
    </g>
    <g class="icon team" fill="none" stroke="var(--white)" stroke-width="4" stroke-linecap="round">
      <circle cx="1141" cy="796" r="11"/>
      <circle cx="1120" cy="806" r="9"/>
      <circle cx="1162" cy="806" r="9"/>
      <path d="M1118 834 q0 -24 23 -24 q23 0 23 24 z"/>
      <path d="M1108 834 q0 -16 8 -19 M1174 834 q0 -16 -8 -19"/>
      <path d="M1141 772 v-6 M1127 776 l-4 -5 M1155 776 l4 -5"/>
    </g>
    <g class="icon growth" fill="none" stroke="var(--white)" stroke-width="4" stroke-linecap="round" stroke-linejoin="round">
      <rect x="752" y="1064" width="12" height="18"/>
      <rect x="772" y="1054" width="12" height="28"/>
      <rect x="792" y="1044" width="12" height="38"/>
      <rect x="812" y="1034" width="12" height="48"/>
      <path d="M752 1050 q40 -14 70 -34 M812 1016 h12 v12"/>
      <circle cx="820" cy="1076" r="8"/>
    </g>
    <g class="icon report" fill="none" stroke="var(--white)" stroke-width="4" stroke-linecap="round" stroke-linejoin="round">
      <path d="M1130 1020 h40 l12 12 v50 h-52 z"/>
      <circle cx="1138" cy="1040" r="14"/>
      <path d="M1138 1026 v14 h14"/>
      <path d="M1160 1040 h14 M1160 1050 h14 M1136 1074 l10 -10 8 6 14 -14"/>
    </g>

    <circle cx="972" cy="950" r="142" fill="url(#core-fill)" stroke="var(--mist)" stroke-width="2"/>
  </svg>

  <p class="hub-title top">COMMUNITY, AQUATIC<br>+ RECREATION FACILITIES</p>
  <p class="hub-title bottom">COMMUNITY ACTIVATION</p>
  <p class="hub-core">COMMUNITY<br>+<br>STAKEHOLDER<br>ENGAGEMENT</p>

  <p class="pillar planning">PLANNING</p>
  <p class="pillar management">MANAGEMENT</p>
  <p class="pillar participation">GROWING<br>PARTICIPATION</p>
  <p class="pillar impact">COMMUNITY<br>IMPACT+OUTCOMES</p>

  <!-- Planning services -->
  <p class="service" style="left:583px; top:359px;">Feacibility Studies</p>
  <p class="service" style="left:506px; top:417px;">Community Research +<span class="cont">Stakeholder</span></p>
  <p class="service" style="left:424px; top:519px;">Sport + Recreation<span class="cont" style="margin-left:-12px;">Strategies</span></p>
  <p class="service" style="left:351px; top:620px;">Design Strategies</p>
  <p class="service" style="left:314px; top:679px;">Indoor + Outdoor Spaces</p>

  <!-- Management services -->
  <p class="service" style="left:1008px; top:359px;">Activating under utilized assets</p>
  <p class="service" style="left:1008px; top:411px;">Income + revenue generation<span class="cont" style="margin-top:-4px;">strategies</span></p>
  <p class="service" style="left:1008px; top:501px;">Mystery shopper + business health checks</p>
  <p class="service" style="left:1008px; top:552px;">Financial + funding strategies</p>
  <p class="service" style="left:1246px; top:613px;">Management support</p>
  <p class="service" style="left:1246px; top:661px;">Business planning</p>

  <!-- Impact services -->
  <p class="service" style="left:1246px; top:986px;">Community impact<span class="cont" style="margin-left:4px;">monitoring</span></p>
  <p class="service" style="left:1246px; top:1079px;">Social Value</p>
  <p class="service" style="left:1246px; top:1135px;">Community outcomes + KPIs</p>
  <p class="service" style="left:1246px; top:1196px;">Contract monitoring</p>

  <!-- Participation services -->
  <p class="service" style="left:306px; top:1038px;">Trends + insights</p>
  <p class="service" style="left:318px; top:1099px;">Health profiling</p>
  <p class="service" style="left:331px; top:1160px;">Active recreation strategies</p>
  <p class="service" style="left:352px; top:1220px;">Community Program<span class="cont" style="margin-left:14px;">Development</span></p>
  <p class="service" style="left:407px; top:1326px;">Physical activity strategies</p>
  <p class="service" style="left:440px; top:1377px;">Specific cohort strategies</p>
  <p class="service" style="left:478px; top:1429px;">Sport + program specific strategies</p>
</main>
</body>
</html>
```